Buch-/E-Book-Cover für Sachbuch über Hunderasse
Zielgruppe
Ich benötige ein Buch-Cover im DIN A5 Format für ein anspruchsvolles Sachbuch, das die rassetypischen Krankheiten der Hunderasse Rhodesian Ridgeback thematisiert. Die Zielgruppe sind Züchter, Tierärzte und Liebhaber der Rasse.
Aufgabenstellung
Den größten Raum sollte ein Foto der Rasse einnehmen. Das Foto würde ich stellen, im Entwurf kann also ein Beispielfoto verwendet werden. Da das Buch der Auftakt zu einer Reihe ist, sollte das Design einen hohen Wiedererkennungswert haben und in erster Linie seriös wirken. Das Foto, der Rassename und die verwendeten Farben sollten leicht austauschbar sein. Sowohl der Titel als auch der Untertitel sind recht lang. Der Arbeitstitel lautet: Stille Pfade im Nebel der Ostseeküste, Untertitel: Geschichten von Fischern und Leuchttürmen.

```html
<!DOCTYPE html>
<html lang="de">
<head>
<meta charset="UTF-8">
<title>Stille Pfade im Nebel der Ostseeküste – Cover</title>
<link href="https://fonts.googleapis.com/css2?family=Archivo:wght@800&family=Work+Sans:wght@400;500&display=swap" rel="stylesheet">
<style>
  :root {
    --navy: #1f2a78;
    --navy-deep: #2a2c7a;
    --dusk: #5a3f80;
    --gold: #ecb422;
    --white: #ffffff;
    --photo-warm: #b8642e;
    --photo-stone: #c9a86a;
    --photo-rose: #a06070;
    --stage-top: #f4f4f8;
    --stage-bottom: #a9aec9;
  }
  * { margin: 0; padding: 0; box-sizing: border-box; }
  html, body { width: 1200px; height: 675px; overflow: hidden; }
  body {
    background: linear-gradient(160deg, var(--stage-top) 30%, var(--stage-bottom) 100%);
    display: flex; align-items: center; justify-content: center;
    font-family: "Work Sans", Arial, sans-serif;
  }
  .cover {
    position: relative;
    width: 424px; height: 600px;
    background: var(--navy);
    overflow: hidden;
    box-shadow: 0 10px 30px rgba(30, 35, 80, 0.25);
  }
  .cover__head {
    position: absolute; left: 0; top: 0;
    width: 100%; height: 215px;
    background: var(--navy);
    padding: 34px 0 0 24px;
    color: var(--white);
  }
  .cover__accent-bar {
    position: absolute; right: 0; top: 0;
    width: 34px; height: 215px;
    background: var(--gold);
  }
  .cover__kicker {
    font-family: "Archivo", Arial, sans-serif;
    font-weight: 800; font-size: 18px; letter-spacing: 0.5px;
    line-height: 1;
  }
  .cover__title {
    font-family: "Archivo", Arial, sans-serif;
    font-weight: 800; font-size: 52px; line-height: 0.98;
    margin-top: 6px; letter-spacing: 0.5px;
  }
  .cover__tagline {
    display: flex; align-items: center; gap: 10px;
    margin-top: 14px;
    color: var(--gold);
    font-weight: 500; font-size: 13px; letter-spacing: 1.6px;
    text-transform: uppercase;
  }
  .cover__tagline svg { flex: none; }
  .cover__photo {
    position: absolute; left: 0; top: 215px;
    width: 100%; height: 385px;
    background:
      linear-gradient(180deg, rgba(42,44,122,0) 35%, rgba(90,63,128,0.75) 62%, var(--navy-deep) 92%),
      radial-gradient(ellipse 55% 60% at 50% 45%, var(--photo-warm) 0%, rgba(184,100,46,0) 100%),
      linear-gradient(180deg, var(--photo-stone) 0%, var(--photo-rose) 70%);
  }
  .cover__subtitle-block {
    position: absolute; left: 0; right: 34px; top: 470px;
    text-align: center; color: var(--white);
  }
  .cover__rule {
    width: 150px; height: 1px; margin: 0 auto;
    background: rgba(255,255,255,0.45);
  }
  .cover__subtitle {
    font-size: 19px; line-height: 1.2; font-weight: 400;
    margin: 12px 0 14px;
  }
  .cover__accent-block {
    position: absolute; right: 0; top: 462px;
    width: 34px; height: 98px;
    background: var(--gold);
  }
</style>
</head>
<body>
  <article class="cover">
    <header class="cover__head">
      <div class="cover__kicker">STILLE</div>
      <h1 class="cover__title">PFADE IM<br>NEBEL</h1>
      <div class="cover__tagline">
        <svg width="26" height="26" viewBox="0 0 26 26" aria-hidden="true">
          <circle cx="13" cy="13" r="10" fill="none" stroke="var(--gold)" stroke-width="1.6"/>
        </svg>
        <span>der Ostseeküste</span>
      </div>
    </header>
    <div class="cover__accent-bar"></div>
    <div class="cover__photo" role="img" aria-label="Titelfoto: Motiv vor warmer Steinmauer, nach unten in Blau verlaufend"></div>
    <div class="cover__subtitle-block">
      <div class="cover__rule"></div>
      <p class="cover__subtitle">Geschichten von Fischern<br>und Leuchttürmen</p>
      <div class="cover__rule"></div>
    </div>
    <div class="cover__accent-block"></div>
  </article>
</body>
</html>
```